Luxury Caviar Tin Label for High End Caviar Retailer

We are looking for a new caviar label design. We want something unique, preferably black and gold or dark blue and gold. We want a modern and luxurious feel. We have several types of caviar so we need to be able to change the name of the caviar when we print the labels. See inspiration attached. Logo is also attached. More about us: kvmarlune.com

Industry/Entity Type

fine foods industry, caviar

Font styles to use
Serif
Decorative

Requirements
Must have
• KV Marlune Logo, space for caviar name
Nice to have
• black and gold, blue and gold

```html
<!DOCTYPE html>
<html lang="en">
<head>
<meta charset="utf-8">
<title>KV Marlune Caviar Tin Label</title>
<link rel="stylesheet" href="https://fonts.googleapis.com/css2?family=Cinzel:wght@600&family=Marcellus&family=Pinyon+Script&family=Source+Serif+4:wght@400&display=swap">
<style>
  :root {
    --navy: #0b1533;
    --gold: #e0a83a;
    --comb-warm: #8a5f3a;
    --comb-cool: #1d2240;
    --paper: #ffffff;
  }
  html, body {
    margin: 0;
    padding: 0;
    width: 1200px;
    height: 1000px;
    overflow: hidden;
    background: var(--paper);
  }
  .label {
    display: block;
    width: 1200px;
    height: 1000px;
  }
  .label-disc { fill: var(--navy); }
  .label-ring { fill: none; stroke: var(--gold); stroke-width: 2; }
  .rim-dot { fill: var(--gold); }
  .rim-text {
    font-family: "Source Serif 4", Georgia, serif;
    font-size: 21px;
    fill: var(--gold);
  }
  .brand-mark { fill: none; stroke: var(--gold); stroke-width: 2.5; }
  .brand-name {
    font-family: "Marcellus", "Times New Roman", serif;
    font-size: 38px;
    fill: var(--gold);
  }
  .product-line {
    font-family: "Cinzel", "Times New Roman", serif;
    font-weight: 600;
    font-size: 56px;
    letter-spacing: 22px;
    fill: var(--gold);
  }
  .variety-name {
    font-family: "Pinyon Script", cursive;
    font-size: 92px;
    fill: var(--gold);
  }
</style>
</head>
<body>
<svg class="label" viewBox="0 0 1200 1000" xmlns="http://www.w3.org/2000/svg">
  <defs>
    <radialGradient id="comb-glow" cx="50%" cy="50%" r="50%">
      <stop offset="0%" stop-color="var(--navy)" stop-opacity="0"/>
      <stop offset="55%" stop-color="var(--comb-cool)" stop-opacity="0.6"/>
      <stop offset="100%" stop-color="var(--comb-warm)" stop-opacity="0.55"/>
    </radialGradient>
    <path id="rim-path" d="M600,144 A356,356 0 1 0 600,856 A356,356 0 1 0 600,144"/>
  </defs>

  <circle class="label-disc" cx="600" cy="500" r="388"/>
  <circle class="label-ring" cx="600" cy="500" r="372"/>
  <circle class="label-ring" cx="600" cy="500" r="320"/>

  <circle class="honeycomb-field" cx="600" cy="500" r="306" fill="url(#comb-glow)"
          role="img" aria-label="Faint gold honeycomb pattern fading toward the centre"/>

  <g class="rim">
    <text class="rim-text"><textPath href="#rim-path" startOffset="205" textLength="348" lengthAdjust="spacing">Ingredients: caviar - salt</textPath></text>
    <text class="rim-text"><textPath href="#rim-path" startOffset="938" textLength="360" lengthAdjust="spacing">Keep refregerated 28 - 34</textPath></text>
    <text class="rim-text"><textPath href="#rim-path" startOffset="1659" textLength="341" lengthAdjust="spacing">www.kvmarlune.com</textPath></text>
    <circle class="rim-dot" cx="434" cy="193" r="5"/>
    <circle class="rim-dot" cx="251" cy="506" r="5"/>
    <circle class="rim-dot" cx="415" cy="796" r="5"/>
    <circle class="rim-dot" cx="785" cy="796" r="5"/>
    <circle class="rim-dot" cx="948" cy="524" r="5"/>
    <circle class="rim-dot" cx="795" cy="211" r="5"/>
  </g>

  <g class="brand">
    <circle class="brand-mark" cx="600" cy="300" r="62"/>
    <text class="brand-name" x="600" y="416" text-anchor="middle">KV MARLUNE</text>
    <text class="product-line" x="611" y="484" text-anchor="middle">CAVIER</text>
  </g>

  <g class="variety">
    <text class="variety-name" x="592" y="608" text-anchor="middle">Beluga</text>
    <text class="variety-name" x="592" y="700" text-anchor="middle">Gold</text>
  </g>
</svg>
</body>
</html>
```